Postcard Design

The Harmony Orchard
An Innovative, Alternative Method Of Healing Body and Mind.
We treat the body from the ‘roots to the branches’ and almost any medical condition can be treated using this approach.

We incorporate various modalities including lifestyle medicine, nutrition, stress, pain management and other approaches.

FUNCTIONAL MEDICINE - Renaldo Cuevas-Amarante, M.D.

We offer services to treat the following but not limited to:
Adrenal Fatigue
Allergies
Autoimmune Diseases
Anxiety/Depression
Chronic Candidiasis
Diabetes & Metabolic Syndrome
Detoxification
Environmental Toxicity
GI Disorders – including Irritable Bowel
Disease (IBS), Crohn’s Disease, Ulcerative Colitis,
Leaky Gut, Food Allergies, and other infectious and inflammatory conditions
Heart Health
Heavy Metal Toxicity
Thyroid Imbalances
Weight Loss

ORIENTAL MEDICINE (ACUPUNCTURE)- Lucia R. Santamar Ochoa, A.P.DOM

We offer Private and Group Acupuncture Treatment up to 5 people per group.
We treat the following conditions and more:
Stress, Anxiety/Depression
Pain Management
Insomnia
Infertility
Facial Acupuncture
Hormone Imbalance
Weight Loss
Chronic Fatigue
Headaches - Including Chronic Migraines, Etc
Updates

Please keep the colors and similar design of previous postcard. You can eliminate some diseases names from the list of Functional Medicine, to keep equal balance between both medicines. Thank you

Target Market(s)

people from Coral Gables (10 - 80 years old) high and medium economic class.

Industry/Entity Type

Medical

```html
<!DOCTYPE html>
<html lang="en">
<head>
<meta charset="utf-8">
<title>The Harmony Orchard – Postcard</title>
<link rel="stylesheet" href="https://fonts.googleapis.com/css2?family=Archivo+Black&family=Arimo:wght@400;700&family=Roboto+Condensed:wght@700&display=swap">
<style>
  :root {
    --backdrop: #5b5b5d;
    --card: #ffffff;
    --teal: #17a99a;
    --mint: #cfe9e3;
    --orange: #f47b3c;
    --coral: #f2785c;
    --ink: #222222;
    --grey-line: #555555;
    --photo-teal: #9fb7b2;
    --photo-warm: #b9886c;
  }
  * { box-sizing: border-box; margin: 0; padding: 0; }
  html, body { width: 1200px; height: 962px; overflow: hidden; }
  body { background: var(--backdrop); font-family: "Arimo", Arial, sans-serif; color: var(--ink); }
  .postcard { position: absolute; left: 80px; top: 83px; width: 1040px; height: 795px; background: var(--card); overflow: hidden; }
  .band { position: absolute; left: 0; background: var(--teal); border-radius: 0 14px 14px 0; color: #fff; }
  .band--functional { top: 32px; width: 712px; height: 93px; }
  .band--oriental { top: 364px; width: 782px; height: 94px; }
  .portrait { position: absolute; left: 44px; width: 146px; height: 172px; border: 5px solid var(--mint); }
  .portrait--functional { top: 45px; background: linear-gradient(160deg, #e8ecea 0%, var(--photo-teal) 55%, #f3f3f3 100%); }
  .portrait--oriental { top: 378px; background: linear-gradient(160deg, #eeeeee 0%, var(--photo-warm) 55%, #f1f1f1 100%); }
  .band__title { position: absolute; left: 216px; font-family: "Archivo Black", "Arial Black", sans-serif; font-size: 33px; letter-spacing: 0.3px; line-height: 1; white-space: nowrap; }
  .band--functional .band__title { top: 17px; }
  .band--oriental .band__title { top: 15px; }
  .band__title small { font-family: "Arimo", Arial, sans-serif; font-weight: 700; font-size: 16px; letter-spacing: 0.3px; }
  .band__name { position: absolute; left: 216px; font-size: 21px; line-height: 1; white-space: nowrap; }
  .band--functional .band__name { top: 60px; }
  .band--oriental .band__name { top: 60px; }
  .band__name strong { font-weight: 700; }
  .intro { position: absolute; color: var(--orange); font-weight: 700; font-size: 22px; line-height: 26px; }
  .intro--functional { left: 736px; top: 44px; }
  .intro--oriental { left: 799px; top: 374px; }
  .conditions { position: absolute; list-style: none; font-size: 20px; line-height: 21px; }
  .conditions li { position: relative; padding-left: 17px; margin-bottom: 7.5px; }
  .conditions li::before { content: ""; position: absolute; left: 0; top: 4px; width: 8px; height: 8px; border-radius: 50%; background: var(--orange); }
  .col-f1 { left: 207px; top: 154px; }
  .col-f2 { left: 469px; top: 154px; }
  .col-f3 { left: 758px; top: 154px; }
  .col-o1 { left: 214px; top: 486px; }
  .col-o2 { left: 517px; top: 486px; }
  .col-o3 { left: 753px; top: 486px; width: 240px; }
  .swoosh { position: absolute; left: 0; top: 600px; }
  .offer { position: absolute; left: 764px; top: 552px; width: 238px; height: 206px; transform: rotate(3deg); }
  .offer__shadow { position: absolute; inset: 8px -6px -8px 6px; background: #bdbdbd; border-radius: 18px; }
  .offer__box { position: absolute; inset: 0; background: var(--coral); border-radius: 18px; color: #fff; text-align: center; padding-top: 22px; }
  .offer__title { font-family: "Arimo", Arial, sans-serif; font-weight: 700; font-size: 35px; line-height: 1; }
  .offer__text { font-family: "Roboto Condensed", "Arial Narrow", sans-serif; font-weight: 700; font-size: 23px; line-height: 24px; margin-top: 14px; }
  .brand { position: absolute; left: 20px; top: 660px; width: 346px; height: 110px; }
  .brand__mark { position: absolute; left: 141px; top: 0; width: 64px; height: 64px; border-radius: 50%; background: var(--teal); }
  .brand__name { position: absolute; left: 0; top: 77px; width: 346px; text-align: center; font-size: 27px; color: var(--grey-line); letter-spacing: 0.5px; white-space: nowrap; }
  .divider { position: absolute; left: 373px; top: 685px; width: 1px; height: 82px; background: #666; }
  .address { position: absolute; left: 391px; top: 708px; font-size: 21px; line-height: 28px; color: var(--ink); font-style: normal; white-space: nowrap; }
</style>
</head>
<body>
  <main class="postcard">
    <section class="service">
      <div class="band band--functional">
        <h1 class="band__title">FUNCTIONAL MEDICINE</h1>
        <p class="band__name"><strong>Renaldo Cuevas-Amarante,</strong> M.D.</p>
      </div>
      <div class="portrait portrait--functional" role="img" aria-label="Portrait photo of Dr. Renaldo Cuevas-Amarante"></div>
      <p class="intro intro--functional">We offer services to<br>treat the following<br>but not limited to:</p>
      <ul class="conditions col-f1">
        <li>Adrenal Fatigue</li>
        <li>Allergies</li>
        <li>Autoimmune Diseases</li>
        <li>Anxiety/Depression</li>
        <li>Chronic Candidiasis</li>
        <li>Diabetes &amp; Metabolic<br>Syndrome</li>
      </ul>
      <ul class="conditions col-f2">
        <li>Detoxification</li>
        <li>Environmental Toxicity</li>
        <li>GI Disorders – including<br>Irritable Bowel</li>
        <li>Disease (IBS), Crohn’s<br>Disease, Ulcerative Colitis,</li>
        <li>Heart Health</li>
      </ul>
      <ul class="conditions col-f3">
        <li>Heavy Metal Toxicity</li>
        <li>Thyroid Imbalances</li>
        <li>Weight Loss</li>
        <li>Leaky Gut, Food<br>Allergies, and other<br>infectious and<br>inflammatory conditions</li>
      </ul>
    </section>

    <section class="service">
      <div class="band band--oriental">
        <h2 class="band__title">ORIENTAL MEDICINE <small>(ACUPUNCTURE)</small></h2>
        <p class="band__name"><strong>Lucia R. Santamar Ochoa,</strong> A.P.DOM</p>
      </div>
      <div class="portrait portrait--oriental" role="img" aria-label="Portrait photo of Lucia R. Santamar Ochoa"></div>
      <p class="intro intro--oriental">We treat the<br>following<br>conditions &amp; more:</p>
      <ul class="conditions col-o1">
        <li>Stress, Anxiety/Depression</li>
        <li>Pain Management</li>
        <li>Insomnia</li>
        <li>Infertility</li>
      </ul>
      <ul class="conditions col-o2">
        <li>Facial Acupuncture</li>
        <li>Hormone Imbalance</li>
        <li>Weight Loss</li>
        <li>Chronic Fatigue</li>
      </ul>
      <ul class="conditions col-o3">
        <li>Headaches - Including<br>Chronic Migraines, Etc</li>
      </ul>
    </section>

    <svg class="swoosh" width="780" height="80" viewBox="0 0 780 80" aria-hidden="true">
      <path d="M0 40 C220 8 520 10 752 36 L752 72 C520 40 240 30 0 42 Z" fill="var(--orange)"/>
      <path d="M300 17 C480 10 640 20 752 30 L752 40 C620 26 470 18 300 17 Z" fill="#555555"/>
    </svg>

    <aside class="offer">
      <div class="offer__shadow"></div>
      <div class="offer__box">
        <p class="offer__title">WE OFFER</p>
        <p class="offer__text">Private and Group<br>Acupuncture<br>Treatment up to 5<br>people per group.</p>
      </div>
    </aside>

    <footer>
      <div class="brand">
        <span class="brand__mark"></span>
        <span class="brand__name">The Harmony Orchard</span>
      </div>
      <span class="divider"></span>
      <address class="address">418 Verbena Court,&nbsp; Suite 210<br>Larkmere Vale, GA 30712</address>
    </footer>
  </main>
</body>
</html>
```